Modern CNC Machining Facility in Need of Web Site Improvement

Brixton Fabrication and Tooling, LLC is in need of a web site update. We need to highlight both product sales and our manufacturing services offered. We have recently started offering online product sales and need a better ecommerce platform for our customers. We would like the design winner to be able to freelance the project to a fully functioning webpage.
www.brixtonfabrication.example
What we like about our current web site:
Black and red highlight colors
Gear and caliper logo
RNVR Veteran owned business
What we don't like about our current web site:
Unorganized
Doesn't stand out
Looks like it was made in 1995
Online Product sales are awkward

```html
<!DOCTYPE html>
<html lang="en">
<head>
<meta charset="utf-8">
<title>Brixton Fabrication and Tooling, LLC</title>
<link rel="stylesheet" href="https://fonts.googleapis.com/css2?family=Oswald:wght@400;500&family=Raleway:wght@400&family=Crimson+Text&family=Open+Sans:wght@400;600&display=swap">
<style>
:root{
  --red:#d01818;
  --red-dark:#8c0c10;
  --brand-red:#b3151c;
  --ink:#222;
  --body:#333;
  --nav:#231f1f;
  --grey-bg:#f0f0f0;
  --line:#d6d6d6;
  --footer:#1c1c1c;
}
*{box-sizing:border-box;margin:0;padding:0}
html,body{width:947px;height:1200px;overflow:hidden;background:#fff}
body{position:relative;font-family:Arial,Helvetica,sans-serif;color:var(--body)}
.abs{position:absolute}

.topbar{left:0;top:0;width:947px;height:28px;border-bottom:1px solid #e6e6e6;background:#fafafa}
.topbar .social{left:92px;top:9px;display:flex;gap:12px}
.topbar .social span{width:9px;height:9px;border-radius:50%;background:#444;display:block}
.topbar .links{right:95px;top:9px;font-size:7.5px;color:#555;display:flex;gap:8px}
.topbar .links b{font-weight:400;color:#bbb}

.brand{left:79px;top:41px;display:flex;align-items:center;gap:10px}
.brand-mark{width:69px;height:69px;border-radius:50%;background:var(--brand-red);border:5px solid #2a2a2a}
.brand-name{font-family:Oswald,sans-serif;font-weight:400;font-size:21px;color:var(--brand-red);letter-spacing:.3px;line-height:1}
.brand-tag{font-family:"Crimson Text",serif;font-size:12px;color:#333;margin-top:8px}

.cart-box{left:700px;top:55px;width:168px;height:40px;border:1px solid #e2e2e2;background:#fff;display:flex;align-items:center;padding-left:10px;gap:8px;font-family:Oswald,sans-serif;font-size:9.5px;color:#333;letter-spacing:.3px}
.cart-box em{font-style:normal;color:var(--red);margin-left:8px}

.nav{left:0;top:121px;width:947px;height:34px;background:var(--nav)}
.nav ul{list-style:none;display:flex;position:absolute;left:82px;top:2px}
.nav li{font-size:10.5px;color:#fff;height:30px;line-height:28px;margin-right:46px}
.nav li.active{background:#f2f2f2;color:#333;padding:0 14px;margin-right:30px;position:relative}
.nav li.active:after{content:"";position:absolute;left:50%;bottom:-5px;margin-left:-5px;border:5px solid transparent;border-top-color:#f2f2f2;border-bottom:0}
.nav .dots{right:96px;top:6px;display:flex;gap:10px}
.nav .dots span{width:22px;height:22px;border-radius:50%;background:#e64628;display:block}

.band{left:0;top:155px;width:947px;height:313px;background:linear-gradient(180deg,var(--red-dark) 0%,var(--red) 55%,#b10f14 100%)}
.stage{left:0;top:468px;width:947px;height:317px;background:linear-gradient(#fff,var(--grey-bg))}
.slide-shadow{left:100px;top:512px;width:740px;height:24px;border-radius:50%;background:radial-gradient(ellipse at center top,rgba(0,0,0,.35),rgba(0,0,0,0) 70%)}
.slide{left:95px;top:193px;width:758px;height:330px;background:#e8e8e8;border:1px solid #ccc;padding:5px}
.slide-photo{width:100%;height:100%;background:linear-gradient(180deg,#c9dcef 0%,#aac3dc 28%,#5d6f86 36%,#d7dde6 55%,#b9c3cf 100%)}
.cap1{left:91px;top:257px;width:313px;height:46px;background:#1f1b1b;font-family:Oswald,sans-serif;font-weight:500;font-size:25px;color:#fff;padding:3px 0 0 15px}
.cap1 span{color:var(--red)}
.cap2{left:91px;top:305px;width:362px;height:40px;background:rgba(192,20,24,.9);font-family:Raleway,sans-serif;font-size:27px;color:#fff;padding:2px 0 0 15px}

.ability-title{left:0;top:555px;width:947px;text-align:center;font-family:Raleway,sans-serif;font-size:29px;color:var(--ink)}
.ability-photo{left:91px;top:614px;width:241px;height:130px;border:3px solid #ccc;background:linear-gradient(135deg,#2a2a2a,#6a4a34 55%,#c49a76)}
.ability-text{left:346px;top:614px;width:520px;font-size:11.3px;line-height:17.5px;color:#333}
.ability-text p+p{margin-top:17.5px}

.divider{left:79px;top:785px;width:789px;height:8px;background:radial-gradient(ellipse at center top,rgba(0,0,0,.18),rgba(0,0,0,0) 70%)}

.products-title{left:79px;top:820px;font-family:Raleway,sans-serif;font-size:28px;color:var(--ink)}
.card{top:872px;width:166px;height:196px;border:1px solid #d8d8d8;background:#fafafa;text-align:center;font-family:"Open Sans",sans-serif}
.card .pic{width:80px;height:80px;margin:12px auto 0;background:linear-gradient(#c8c8c8,#6d6d6d);border-radius:3px}
.card .name{margin-top:14px;font-size:10px;line-height:13px;color:#c33}
.card .name span{display:block;color:#333}
.card .price{font-size:17.5px;color:#333;margin-top:6px}
.card .btn{display:inline-block;margin-top:5px;width:86px;height:21px;line-height:19px;background:var(--red);border:1px solid #fff;outline:1px solid var(--red);color:#fff;font-weight:600;font-size:11px}

.footer{left:0;top:1107px;width:947px;height:93px;border-top:3px solid var(--red);background:linear-gradient(#2a2a2a,var(--footer))}
.partners{left:230px;top:20px;display:flex;gap:16px;align-items:center}
.partners span{display:block;height:14px;background:#555;border-radius:2px}
.flinks{left:0;top:50px;width:947px;text-align:center;font-family:"Open Sans",sans-serif;font-size:10px;color:#ddd;letter-spacing:.4px}
.copy{left:0;top:72px;width:947px;text-align:center;font-family:"Open Sans",sans-serif;font-size:10px;color:#ccc;letter-spacing:.4px}
</style>
</head>
<body>

<div class="topbar abs">
  <div class="social abs"><span></span><span></span><span></span><span></span><span></span></div>
  <div class="links abs">Shop <b>|</b> My Account <b>|</b> Checkout <b>|</b>
    <svg width="10" height="8" viewBox="0 0 10 8"><path d="M0 1h2l1 5h6l1-4H3" fill="none" stroke="#666" stroke-width="1"/></svg>0 items - R0</div>
</div>

<div class="brand abs">
  <div class="brand-mark"></div>
  <div>
    <div class="brand-name">Brixton Fabrication and Tooling, LLC</div>
    <div class="brand-tag">CNC Milling &amp; Turning, Production Machining, Ice Fishing Spears</div>
  </div>
</div>

<div class="cart-box abs">
  <svg width="26" height="22" viewBox="0 0 26 22"><path d="M1 2h4l3 12h14l3-9H7" fill="none" stroke="#c01818" stroke-width="2.5"/><circle cx="10" cy="19" r="2" fill="#c01818"/><circle cx="20" cy="19" r="2" fill="#c01818"/></svg>
  SHOPPING CART: <em>0 items</em>
</div>

<nav class="nav abs">
  <ul>
    <li class="active">HOME</li>
    <li>ONLINE PRODUCT SALES</li>
    <li>ICE FISHING SPEARS</li>
    <li>ABOUT US</li>
    <li>CONTACT US</li>
  </ul>
  <div class="dots abs"><span style="background:#3b5a9a"></span><span style="background:#2a9ad6"></span><span></span><span style="background:#f0781e"></span></div>
</nav>

<div class="band abs"></div>
<div class="stage abs"></div>
<div class="slide-shadow abs"></div>
<div class="slide abs"><div class="slide-photo" role="img" aria-label="Ice fisherman in a yellow snowsuit seated beside a hole on a frozen lake"></div></div>
<div class="cap1 abs">Our Manufacturing <span>Ability</span></div>
<div class="cap2 abs">Our Online Products Sales</div>

<h2 class="ability-title abs" style="font-weight:400">Our Manufacturing Ability</h2>
<div class="ability-photo abs" role="img" aria-label="Close-up of hands working a piece on a lathe with chips flying"></div>
<div class="ability-text abs">
  <p>We are your CNC milling and turning go-to facility. Our manufacturing facility is located in Harlow Bay, Michigan and is equipped to perform a variety of machining services, including three axis CNC milling, "lights out" CNC turning, CNC Plasma Cutting, fully automatic sawing, prototype machining, long and short run production.</p>
  <p>Brixton Fabrication is proudly owned and operated by Daniel and Peter Marsh. We have the capability, experience and know-how to solve even your most complex manufacturing problems.</p>
</div>

<div class="divider abs"></div>

<h2 class="products-title abs" style="font-weight:400">Our Products</h2>

<div class="card abs" style="left:82px"><div class="pic" role="img" aria-label="Ice fishing spear head"></div><div class="name">Talon 230 Blade 9 X 48T<span>X 1 For Cutting Steel</span></div><div class="price">$99.99</div><div class="btn">Add Cart</div></div>
<div class="card abs" style="left:288px"><div class="pic" role="img" aria-label="Wide ice fishing spear head"></div><div class="name">Talon 230 Blade 9 X 48T<span>X 1 For Cutting Steel</span></div><div class="price">$99.99</div><div class="btn">Add Cart</div></div>
<div class="card abs" style="left:493px"><div class="pic" role="img" aria-label="Ice fishing spear head"></div><div class="name">Talon 230 Blade 9 X 48T<span>X 1 For Cutting Steel</span></div><div class="price">$99.99</div><div class="btn">Add Cart</div></div>
<div class="card abs" style="left:697px"><div class="pic" role="img" aria-label="Wide ice fishing spear head"></div><div class="name">Talon 230 Blade 9 X 48T<span>X 1 For Cutting Steel</span></div><div class="price">$99.99</div><div class="btn">Add Cart</div></div>

<footer class="footer abs">
  <div class="partners abs"><span style="width:46px"></span><span style="width:62px"></span><span style="width:40px"></span><span style="width:26px"></span><span style="width:54px"></span><span style="width:64px"></span><span style="width:54px"></span></div>
  <div class="flinks abs">Home | Login | Specials | Shopping Cart | Checkout | Contact us | Terms | Privacy Notice | Shipping</div>
  <div class="copy abs">Copyright Brixton Fabrication &amp; Tooling, 2014</div>
</footer>

</body>
</html>
```